Business Card for supplement company

Company Name: Brimcrest Nutrition
We require quite a simple yet stand out business card for our supplement company.
We are selling high end bodybuilding supplements direct to the public through online sales and Facebook marketing.
There will be slightly varying versions of the card and the winning design will be required to make these slight adjustments.
We will also require the file to be provided in and editable version as we will have a discount code on there that will be changed for different people.
Employee Cards:
Logo on the front of the card (see attached EPS file)
Please also add slogan in text "When Failure is Not and Option" as close as possible to what is seen in this link www.brimcrestnutrition.example.com.au
Suggestions: Card in black, possibly use a similar background to website theme (honeycomb, carbon look)
Information to be included on the back (please place and order accordingly)
:Tarq Welmsby (Director)
Email: tarq@brimcrestnutrition.example.com.au
Phone: 02 5918 2273
Website: www.brimcrestnutrition.example.com.au
Athlete Cards:
Front:
Same as above
Back:
Discount Code: xxx123 (to be editable)
Facebook: www.socialsite.example/BrimcrestNutrition
Design ideas: please look at our website and facebook signup page for design ideas.

```html
<!DOCTYPE html>
<html lang="en">
<head>
<meta charset="utf-8">
<title>Brimcrest Nutrition – Business Card</title>
<link rel="stylesheet" href="https://fonts.googleapis.com/css2?family=Lato:wght@400;700;900&display=swap">
<style>
  :root {
    --backdrop: #e7e4e0;
    --card: #2a2a2a;
    --brand-green: #4caf3a;
    --rule-green: #3f9a32;
    --accent-yellow: #e2c21c;
    --light: #e6e6e6;
  }
  * { box-sizing: border-box; margin: 0; padding: 0; }
  html, body {
    width: 1200px; height: 900px; overflow: hidden;
    background: var(--backdrop);
    font-family: "Lato", Arial, sans-serif;
  }
  .canvas { position: relative; width: 1200px; height: 900px; }
  .card {
    position: absolute; left: 354px; width: 488px; height: 278px;
    background: var(--card);
    border-radius: 12px;
    box-shadow: 0 3px 8px rgba(0,0,0,.35);
    overflow: hidden;
  }
  .card--front { top: 154px; }
  .card--back { top: 464px; }

  .brand {
    position: absolute; left: 0; right: 0; top: 78px;
    text-align: center; color: var(--brand-green); font-weight: 900;
  }
  .brand__name { display: block; font-size: 54px; line-height: 60px; letter-spacing: 1px; }
  .brand__descriptor { display: block; font-size: 19px; letter-spacing: 6px; margin-top: 4px; }

  .tagline {
    position: absolute; left: 0; right: 0; top: 200px;
    display: flex; align-items: center; gap: 26px;
    color: var(--accent-yellow); font-size: 15px; white-space: nowrap;
  }
  .tagline__rule { flex: 1; height: 1px; background: var(--rule-green); }

  .contact-person {
    position: absolute; left: 0; right: 0; top: 98px; text-align: center;
  }
  .contact-person__name { color: var(--brand-green); font-weight: 700; font-size: 17px; line-height: 22px; }
  .contact-person__role { color: var(--accent-yellow); font-size: 13px; line-height: 18px; }

  .contact-details {
    position: absolute; left: 0; right: 0; top: 180px;
    display: flex; justify-content: center; align-items: center; gap: 14px;
  }
  .contact-details__bar { width: 1px; height: 15px; background: var(--rule-green); }
  .contact-details__list {
    list-style: none; text-align: center;
    color: var(--accent-yellow); font-size: 14px; line-height: 19.5px;
  }
</style>
</head>
<body>
<main class="canvas">
  <section class="card card--front" aria-label="Card front">
    <h1 class="brand">
      <span class="brand__name">BRIMCREST</span>
      <span class="brand__descriptor">NUTRITION</span>
    </h1>
    <p class="tagline">
      <span class="tagline__rule"></span>
      When Failure is Not and Option
      <span class="tagline__rule"></span>
    </p>
  </section>

  <section class="card card--back" aria-label="Card back">
    <div class="contact-person">
      <p class="contact-person__name">Tarq Welmsby</p>
      <p class="contact-person__role">DIRECTOR</p>
    </div>
    <div class="contact-details">
      <span class="contact-details__bar"></span>
      <ul class="contact-details__list">
        <li>02 5918 2273</li>
        <li>tarq@brimcrestnutrition.example.com.au</li>
        <li>www.brimcrestnutrition.example.com.au</li>
      </ul>
      <span class="contact-details__bar"></span>
    </div>
  </section>
</main>
</body>
</html>
```